ATTORNEY FULL PAGE AD

We need a full page flyer for our law firm. We are sending it to people who were in an auto accident and injured. I want to let people know that by hiring an attorney that does not mean that they are suing someone. We will just help them in filing a claim and to get them compensated for: medical bills, lost wages, car repairs, future medical treatment or surgery, and pain/suffering. They will NOT have to pay us any money unless we get them paid. I want to show that we are compassionate to the fact that they went through this tramatic event that will effect their lives for ever. They do not have to worry about anything once they hire us. Our website is: www.brightwelllawfirm.com Our colors are black and gold. NO GAMBLING REFERENCES!!!!
Updates

Don't worry so much about content and wording. Once we get a design and images that look great we will message you the exact words we would like put into the paragraphs. The overall "look" and images are the most important. If anyone has a great change-up logo we are open to it as well. Thanks for everyone's hard work!

We like the dark colors. Some of the images are a little cheesy. We are a family business and treat are clients as family. I like the pictures o the car crashes an the hands. No blood. We want to come off as respectful and trustworthy. It's more about how we will care for them as family than getting them lots of money. 

Target Market(s)

People who were in major accidents and have serious injuries

Industry/Entity Type

Attorney

Requirements
Must have
• Must have our phone number: 1-855-MBRIGHT
Website: www.brightwelllawfirm.com
Company name: Brightwell Law Group
Attorney name: Morgan Ellis Brightwell
High gloss with card stock paper.
Classy - NOT cheesy
Should not have
• No cartoons. Very masculine and professional. There may have been death involved in the accident so we want the ad to be very compassionate and moving.

```html
<!DOCTYPE html>
<html lang="en">
<head>
<meta charset="utf-8">
<title>Brightwell Law Group – Flyer</title>
<link rel="stylesheet" href="https://fonts.googleapis.com/css2?family=Federo&family=Ubuntu:wght@400&family=Cutive+Mono&display=swap">
<style>
  :root {
    --ink: #000000;
    --peach: #f7b98c;
    --peach-soft: #f2c29b;
    --copper: #9a4f1f;
    --copper-deep: #4a2410;
    --photo-border: #f4f1ec;
    --photo-border-warm: #e6cdb5;
  }
  * { margin: 0; padding: 0; box-sizing: border-box; }
  html, body { width: 846px; height: 1200px; overflow: hidden; background: var(--ink); }
  .flyer {
    position: relative; width: 846px; height: 1200px; overflow: hidden;
    background: var(--ink);
    font-family: "Ubuntu", sans-serif; color: var(--peach-soft);
  }
  .flourish-field {
    position: absolute; inset: 0;
    background:
      radial-gradient(ellipse 60% 40% at 15% 30%, rgba(154,79,31,0.28), transparent 70%),
      radial-gradient(ellipse 50% 40% at 85% 55%, rgba(154,79,31,0.26), transparent 70%),
      radial-gradient(ellipse 60% 35% at 50% 85%, rgba(154,79,31,0.24), transparent 70%),
      linear-gradient(180deg, #0b0402, #120703 50%, #0b0402);
  }
  .wordmark {
    position: absolute; top: 22px; left: 0; width: 100%;
    text-align: center; font-family: "Federo", sans-serif; color: var(--peach);
  }
  .wordmark-name { font-size: 74px; letter-spacing: 12px; line-height: 90px; padding-left: 12px; }
  .wordmark-rule { position: absolute; top: 109px; left: 0; width: 846px; height: 20px; }
  .wordmark-sub {
    position: absolute; top: 98px; left: 0; width: 100%;
    font-size: 22px; letter-spacing: 4px; line-height: 40px;
  }
  .frame-lines { position: absolute; inset: 0; }
  .copy { position: absolute; left: 30px; width: 786px; text-align: center; }
  .copy-small { font-size: 16.5px; line-height: 24px; }
  .copy-cta { font-size: 20.5px; line-height: 30px; color: var(--peach); }
  .intro { top: 208px; }
  .approach { top: 296px; }
  .practice { top: 380px; }
  .consult { top: 459px; }
  .results { top: 808px; font-size: 25px; line-height: 36px; color: var(--peach); }
  .photo {
    position: absolute; padding: 8px; background: var(--photo-border);
    box-shadow: 2px 3px 6px rgba(0,0,0,0.6);
  }
  .photo-fill { width: 100%; height: 100%; }
  .photo-courthouse { left: 80px; top: 582px; width: 236px; height: 172px; transform: rotate(-3deg); }
  .photo-courthouse .photo-fill { background: linear-gradient(180deg, #2b4f8a, #8aa4c4 45%, #d8d6d0 60%, #9b9a94); }
  .photo-scene { left: 318px; top: 558px; width: 232px; height: 180px; background: var(--photo-border-warm); }
  .photo-scene .photo-fill { background: linear-gradient(180deg, #6d5a3c, #c9c4bd 40%, #7a8f5a 65%, #5d8a3a); }
  .photo-book { left: 554px; top: 580px; width: 228px; height: 186px; transform: rotate(3.5deg); }
  .photo-book .photo-fill { background: radial-gradient(ellipse at 55% 60%, #8a2a22, #c9b8a8 55%, #ffffff 80%); }
  .contact-frame { position: absolute; left: 232px; top: 900px; width: 410px; height: 222px; }
  .contact {
    position: absolute; left: 232px; top: 962px; width: 410px;
    text-align: center; font-size: 31px; line-height: 36px; color: var(--peach);
  }
  .website {
    position: absolute; top: 1138px; left: 0; width: 100%; text-align: center;
    font-family: "Cutive Mono", monospace; font-size: 27px; letter-spacing: 2.5px; color: var(--peach);
  }
</style>
</head>
<body>
<main class="flyer">
  <div class="flourish-field" role="img" aria-label="Black background covered with copper-brown curling vine flourishes"></div>

  <svg class="frame-lines" width="846" height="1200" viewBox="0 0 846 1200" aria-hidden="true">
    <rect x="14" y="180" width="5" height="956" fill="#f7b98c"/>
    <circle cx="28" cy="1168" r="13" fill="#f7b98c"/>
    <rect x="56" y="1172" width="764" height="6" fill="#f7b98c"/>
  </svg>

  <header class="wordmark">
    <div class="wordmark-name">BRIGHTWELL</div>
    <svg class="wordmark-rule" width="846" height="20" viewBox="0 0 846 20" aria-hidden="true">
      <path d="M30 10 L250 8 L250 12 Z" fill="#f7b98c"/>
      <circle cx="265" cy="10" r="4" fill="#f7b98c"/>
      <circle cx="582" cy="10" r="4" fill="#f7b98c"/>
      <path d="M597 8 L816 10 L597 12 Z" fill="#f7b98c"/>
    </svg>
    <div class="wordmark-sub">Law Group</div>
  </header>

  <p class="copy copy-small intro">At Brightwell Law Group, we sincerely care about our clients. When you step into our office,<br>you become family, and we fight hard to win our family the recovery it deserves.</p>
  <p class="copy copy-small approach">Brightwell Law Group offers no frills or gimmicks. Just smart, aggressive representation<br>with a fighter's mentality. Get us in your corner for the best chance at victory.</p>
  <p class="copy copy-small practice">Brightwell Law Group handles a wide variety of personal injury cases, including DUI,<br>automobile accidents, medical malpractice and worker's comp</p>
  <p class="copy copy-cta consult">Brightwell Law Group will review your case free of charge. Stop by our<br>Savannah office or call 855-MBRIGHT for a FREE CONSULTATION today.</p>

  <figure class="photo photo-courthouse"><div class="photo-fill" role="img" aria-label="Photo of a columned courthouse under a blue sky"></div></figure>
  <figure class="photo photo-scene"><div class="photo-fill" role="img" aria-label="Photo of emergency crews at a car accident beside a tree"></div></figure>
  <figure class="photo photo-book"><div class="photo-fill" role="img" aria-label="Photo of a gavel resting on a red law book"></div></figure>

  <p class="copy results">Brightwell Law Group has earned millions of dollars for its<br>accident victims, garnering headlines and TV news coverage</p>

  <svg class="contact-frame" width="410" height="222" viewBox="0 0 410 222" aria-hidden="true">
    <rect x="6" y="6" width="398" height="210" rx="28" fill="none" stroke="#f7b98c" stroke-width="4"/>
    <rect x="20" y="20" width="370" height="182" rx="20" fill="none" stroke="#f7b98c" stroke-width="1.5"/>
  </svg>
  <address class="contact" style="font-style:normal">1-855-MBRIGHT<br>Morgan Ellis<br>Brightwell</address>

  <div class="website">www.brightwelllawfirm.com</div>
</main>
</body>
</html>
```